Quellmoor Medical Center Wall Mural

I need to design a wall mural for an interior wall measuring 3 meters by 20 meters. that includes either all of the services provided or a map of the locations listed on this webpage https://www.quellmoor-medical.org/locations. It just needs to be very creative.

Executives

```html
<!DOCTYPE html>
<html lang="en">
<head>
<meta charset="utf-8">
<title>Quellmoor Medical Center – Services Mural</title>
<link href="https://fonts.googleapis.com/css2?family=Red+Hat+Display:wght@500&display=swap" rel="stylesheet">
<style>
  :root {
    --red: #d4102b;
    --black: #131313;
    --text: #ffffff;
    --bg-light: #e8eef2;
    --bg-blue: #b9cfdc;
    --map-green: #cfe5d3;
    --map-sand: #ece8d8;
    --pin: #e0202f;
  }
  html, body {
    margin: 0;
    width: 1200px;
    height: 180px;
    overflow: hidden;
  }
  .mural {
    position: relative;
    width: 1200px;
    height: 180px;
    background: linear-gradient(90deg, var(--bg-blue) 0%, var(--bg-light) 25%, var(--bg-light) 75%, var(--bg-blue) 100%);
    font-family: "Red Hat Display", sans-serif;
    font-weight: 500;
    overflow: hidden;
  }
  .location-map {
    position: absolute;
    left: 310px;
    top: 0;
    width: 560px;
    height: 180px;
    background:
      linear-gradient(90deg, var(--bg-light) 0%, transparent 12%, transparent 88%, var(--bg-light) 100%),
      linear-gradient(120deg, var(--map-sand) 0%, var(--map-green) 40%, var(--map-green) 70%, var(--map-sand) 100%);
  }
  .location-pins {
    position: absolute;
    left: 0;
    top: 0;
  }
  .service-column {
    position: absolute;
    top: 12px;
    display: flex;
    flex-direction: column;
    gap: 4.9px;
  }
  .service {
    height: 15px;
    width: 112px;
    padding-left: 10px;
    box-sizing: border-box;
    display: flex;
    align-items: center;
    color: var(--text);
    font-size: 7px;
    white-space: nowrap;
  }
  .service.small { font-size: 5.6px; }
  .service.tight { padding-left: 7px; }
  .red   { background: linear-gradient(90deg, var(--red) 0%, var(--red) 62%, rgba(212,16,43,0) 100%); }
  .black { background: linear-gradient(90deg, var(--black) 0%, var(--black) 62%, rgba(19,19,19,0) 100%); }
</style>
</head>
<body>
<main class="mural">
  <div class="location-map" role="img" aria-label="Map of Quellmoor Medical Center locations across the region"></div>

  <svg class="location-pins" width="1200" height="180" viewBox="0 0 1200 180" aria-hidden="true">
    <defs>
      <g id="pin">
        <path d="M0 16 C-2 11 -6 8 -6 4 A6 6 0 0 1 6 4 C6 8 2 11 0 16 Z" fill="var(--pin)"/>
        <circle cx="0" cy="4" r="2.1" fill="#8a0d1a"/>
      </g>
    </defs>
    <use href="#pin" x="563" y="30"/>
    <use href="#pin" x="597" y="27"/>
    <use href="#pin" x="619" y="23"/>
    <use href="#pin" x="583" y="53"/>
    <use href="#pin" x="597" y="53"/>
    <use href="#pin" x="589" y="71"/>
    <use href="#pin" x="622" y="71"/>
    <use href="#pin" x="609" y="108"/>
  </svg>

  <div class="service-column" style="left:9px">
    <div class="service red small tight">Cancer and Hematology Treatment</div>
    <div class="service black">Cardiac Rehab</div>
    <div class="service red">Cardiovascular</div>
    <div class="service black">Care Management</div>
    <div class="service red">Critical Care Unit</div>
    <div class="service black">Dermatology</div>
    <div class="service red">Diabetes Care Services</div>
    <div class="service black">Emergency Care</div>
  </div>

  <div class="service-column" style="left:121px">
    <div class="service black">Endocrinology</div>
    <div class="service red">Endoscopy</div>
    <div class="service black">Family Medicine</div>
    <div class="service red">Fitness Center</div>
    <div class="service black">Gastroenterology</div>
    <div class="service red">General Surgery</div>
    <div class="service black small">Home Care Services/Hospice</div>
    <div class="service red">In-Patient Rehabilitation</div>
  </div>

  <div class="service-column" style="left:232px">
    <div class="service red">Internal Medicine</div>
    <div class="service black">Joint Replacement</div>
    <div class="service red">Labor &amp; Delivery</div>
    <div class="service black">Laboratory Services</div>
    <div class="service red">Medical Care Unit</div>
    <div class="service black">Medical Supplies</div>
    <div class="service red">Neurology</div>
    <div class="service black">Nursing Services</div>
  </div>

  <div class="service-column" style="left:854px">
    <div class="service black">Nutrition</div>
    <div class="service red">Obstetrics/Gynecology</div>
    <div class="service black">Occupational Medicine</div>
    <div class="service red">Ophthalmology</div>
    <div class="service black">Orthopedic Care</div>
    <div class="service red">Otolaryngology (ENT)</div>
    <div class="service black small">Out-Patient Infusion Services</div>
    <div class="service red">Out-Patient Rehabilitation</div>
  </div>

  <div class="service-column" style="left:965px">
    <div class="service red">Pediatrics</div>
    <div class="service black">Physical Therapy</div>
    <div class="service red">Psychiatry &amp; Counseling</div>
    <div class="service black">Pulmonary Function Testing</div>
    <div class="service red">Radiology</div>
    <div class="service black">Respite/Custodial Care</div>
    <div class="service red">Sleep Medicine</div>
    <div class="service black">Spine Surgery</div>
  </div>

  <div class="service-column" style="left:1077px">
    <div class="service black small">Quellmoor Collaborative Care</div>
    <div class="service red">Stroke Treatment</div>
    <div class="service black">Surgical Services</div>
    <div class="service red">Telemedicine</div>
    <div class="service black">Urgent Care</div>
    <div class="service red">Urology</div>
    <div class="service black">Wound Care</div>
    <div class="service red">And More</div>
  </div>
</main>
</body>
</html>
```